Corvenix Business Card

Our mission is to craft high value solutions combining consulting and edge technologies for helping big and middle sized companies in the Digital Transformation Process that they must face. We think that this transformation will impact business processes and people skills in a new manner. Corvenix's value proposition is to collaborate with our clients for creating new competitive advantages based on technology, processes and people.
We already have a logo designed through your platform.

Industry/Entity Type

Business

```html
<!DOCTYPE html>
<html lang="en">
<head>
<meta charset="utf-8">
<title>Corvenix Business Card</title>
<link rel="stylesheet" href="https://fonts.googleapis.com/css2?family=Open+Sans:wght@400;600;700&display=swap">
<style>
  :root {
    --bg: #2b2b2d;
    --card-dark: #434346;
    --card-dark-edge: #333336;
    --card-light: #ffffff;
    --ink: #2a2a2c;
    --ink-soft: #3c3c3e;
    --muted-on-dark: #d9d9dc;
    --accent: #1b95cf;
    --silver: #b9babd;
  }
  * { box-sizing: border-box; margin: 0; padding: 0; }
  html, body { width: 1200px; height: 860px; overflow: hidden; }
  body {
    background: var(--bg);
    font-family: "Open Sans", Arial, sans-serif;
    position: relative;
  }
  .card {
    position: absolute;
    width: 525px;
    height: 300px;
    border-radius: 22px;
    overflow: hidden;
    box-shadow: 0 14px 30px rgba(0,0,0,.45);
  }
  /* Back side */
  .card-back {
    left: 50px;
    top: 280px;
    background: linear-gradient(180deg, var(--card-dark) 0%, var(--card-dark-edge) 100%);
    color: var(--muted-on-dark);
    text-align: center;
  }
  .card-back .brand {
    margin-top: 72px;
    font-size: 30px;
    font-weight: 600;
    letter-spacing: 3px;
    color: var(--accent);
  }
  .card-back .tagline {
    margin-top: 18px;
    font-size: 17px;
    letter-spacing: .4px;
  }
  .card-back .web {
    margin-top: 40px;
    font-size: 15px;
    letter-spacing: 2.5px;
  }
  /* Front side */
  .card-front {
    left: 625px;
    top: 280px;
    background: var(--card-light);
    color: var(--ink);
  }
  .card-front .swoosh { position: absolute; inset: 0; }
  .brand-row {
    position: absolute;
    left: 40px;
    top: 34px;
    display: flex;
    align-items: center;
    gap: 14px;
  }
  .brand-dot {
    width: 40px; height: 40px;
    border-radius: 50%;
    background: var(--accent);
  }
  .brand-row .brand {
    font-size: 36px;
    font-weight: 600;
    letter-spacing: 2px;
    color: var(--ink);
  }
  .address {
    position: absolute;
    left: 44px;
    top: 108px;
    font-size: 13px;
    line-height: 1.4;
    color: var(--ink-soft);
  }
  .contacts {
    position: absolute;
    left: 28px;
    top: 160px;
    list-style: none;
    font-size: 15px;
    line-height: 1.6;
    color: var(--ink);
  }
  .contacts li { display: flex; align-items: center; gap: 6px; }
  .contacts svg { width: 14px; height: 14px; flex: none; }
  .person {
    position: absolute;
    left: 300px;
    top: 178px;
  }
  .person .name {
    font-size: 15px;
    font-weight: 700;
    color: var(--accent);
    letter-spacing: .3px;
  }
  .person .role {
    font-size: 13px;
    color: var(--ink);
  }
</style>
</head>
<body>

<section class="card card-back">
  <div class="brand">CORVENIX</div>
  <p class="tagline">Shaping Progress for a Connected Age</p>
  <p class="web">www.corvenix.com</p>
</section>

<section class="card card-front">
  <svg class="swoosh" viewBox="0 0 525 300" preserveAspectRatio="none" aria-hidden="true">
    <path d="M430 0 C500 50 525 150 525 210 L525 0 Z" fill="var(--silver)"/>
    <path d="M250 300 C420 270 500 180 470 20 C515 90 525 160 525 200 L525 300 Z" fill="var(--accent)"/>
  </svg>

  <div class="brand-row">
    <span class="brand-dot"></span>
    <span class="brand">CORVENIX</span>
  </div>

  <p class="address">27.4th floor, Tower<br>Harbor Lane QNT</p>

  <ul class="contacts">
    <li>
      <svg viewBox="0 0 24 24"><path fill="var(--accent)" d="M6.6 10.8a15.1 15.1 0 006.6 6.6l2.2-2.2c.3-.3.7-.4 1-.2 1.1.4 2.3.6 3.6.6.6 0 1 .4 1 1V20c0 .6-.4 1-1 1A17 17 0 013 4c0-.6.4-1 1-1h3.5c.6 0 1 .4 1 1 0 1.3.2 2.5.6 3.6.1.3 0 .7-.2 1z"/></svg>
      014 672 3095
    </li>
    <li>
      <svg viewBox="0 0 24 24"><rect x="2" y="5" width="20" height="14" rx="2" fill="var(--accent)"/><path d="M3 6l9 7 9-7" fill="none" stroke="#fff" stroke-width="1.6"/></svg>
      hello@corvenix.com
    </li>
    <li>
      <svg viewBox="0 0 24 24"><g fill="none" stroke="var(--accent)" stroke-width="2"><circle cx="12" cy="12" r="9.5"/><ellipse cx="12" cy="12" rx="4" ry="9.5"/><path d="M2.5 12h19M4 7h16M4 17h16"/></g></svg>
      www.corvenix.com
    </li>
  </ul>

  <div class="person">
    <p class="name">MARCUS HALE</p>
    <p class="role">Managing Director</p>
  </div>
</section>

</body>
</html>
```